New letterhead/ stationary design for insurance restoration builder

Modern, clever creative not cheap tacky design maroon and black / white are logo colours. Company name is Harbor Peak Building Services. Might need two different versions of new design, one for standard letterhead communicatio, the other i need to use for management aystems policies amd procedirrs etc.becauuse you wong have tome
Target Market(s)
Large residential insurance companies and their clients, tradespeople and the integrated management system with policies and procedures is internal company employees.
Font styles to use
Requirements
Must have
- A version that would be used as a typical business letterhead is and the other needs to be in a format / design that suits company policies and procedures. Be professional, HARBOR PEAK and be creative / totally custom for pur business not just an edited version of what you can get for free in Word or off the internet pls. Incorporating industry relevant shapes or placement to create the illusion of a residential construction related image is an idea. Someone who is cleverly creative with simple but impactdul design will get my interest.
Nice to have
- Can have different shades of the corporate colours used which are maroon / burgundy and black. https://fernlowmedia.example/common/images/v3/sketch-icon-dropzone.png
Should not have
- Look like the genetic templates and designs you can do yourself copying off the internet.

```html
<!DOCTYPE html>
<html lang="en">
<head>
<meta charset="utf-8">
<title>Harbor Peak Building Services – Letterhead</title>
<link href="https://fonts.googleapis.com/css2?family=Open+Sans:wght@400;600;800&family=Lato:wght@400;700&family=Arimo:wght@400;700&display=swap" rel="stylesheet">
<style>
  :root {
    --maroon: #9b0a46;
    --accent: #c8185a;
    --ink: #3a3a3a;
    --black: #050505;
    --white: #ffffff;
    --faint: #ececec;
    --backdrop: #e4e4e6;
  }
  html, body { margin: 0; padding: 0; overflow: hidden; }
  body {
    width: 1040px; height: 1200px;
    background: var(--backdrop);
    font-family: "Open Sans", sans-serif;
    color: var(--ink);
  }
  p { margin: 0; }
  .letterhead {
    position: absolute; left: 70px; top: 15px;
    width: 900px; height: 1170px;
    background: var(--white);
    overflow: hidden;
  }
  .brand {
    position: absolute; left: 56px; top: 44px;
    font-weight: 800; font-size: 30px; line-height: 34px;
    color: var(--maroon);
  }
  .watermark {
    position: absolute; left: 207px; top: 770px;
    font-weight: 800; font-size: 86px; line-height: 88px;
    color: var(--faint); letter-spacing: -2px;
  }
  .letter { position: absolute; left: 56px; width: 550px; font-size: 14.5px; line-height: 17px; margin: 0; }
  .date { top: 220px; }
  .recipient { top: 255px; }
  .salutation { top: 355px; }
  .body-text { line-height: 26px; text-align: justify; }
  .para-1 { top: 401px; }
  .para-2 { top: 632px; }
  .closing { top: 765px; }
  .signatory { top: 838px; }
  .signatory .name { font-size: 18px; line-height: 22px; font-weight: 600; color: #2a2a2a; }
  .signatory .role { margin-top: 6px; }
  .contact-bar {
    position: absolute; left: 56px; top: 1119px; width: 580px;
    font-family: "Arimo", sans-serif; font-size: 15px; color: #222;
    white-space: nowrap;
  }
  .contact-bar b { color: var(--maroon); }
  .contact-bar .sep { margin: 0 5px; }
  .contact-bar .domain { color: var(--maroon); }
  .office-rail {
    position: absolute; left: 660px; top: 0; width: 240px; height: 100%;
    background: var(--black);
    font-family: "Lato", sans-serif; font-size: 14.5px; line-height: 17px;
    color: var(--white);
  }
  .office { position: absolute; left: 38px; white-space: nowrap; }
  .office h3 {
    margin: 0; font-size: 14.5px; font-weight: 700;
    color: var(--accent); text-transform: uppercase; letter-spacing: -0.2px;
  }
  .office .label { color: var(--accent); }
  .office-head { top: 397px; }
  .office-north { top: 555px; }
  .office-west { top: 690px; }
  .office-river { top: 825px; }
  .rule { position: absolute; left: 40px; width: 61px; height: 1px; background: var(--maroon); }
</style>
</head>
<body>
<main class="letterhead">
  <p class="brand">Harbor Peak<br>Building Services</p>
  <p class="watermark" aria-hidden="true">Harbor<br>Peak</p>

  <p class="letter date">Issuing Date: May 5, 2018</p>
  <div class="letter recipient">
    <p>Name Of Employee Mr. XYZABC</p>
    <p>Address of Employee</p>
    <p>Address Line 2 etc..</p>
  </div>
  <p class="letter salutation">Dear Mr.XYZABC</p>
  <p class="letter body-text para-1">Lorem Ipsum has been the industry's standard dummy text ever since the 1500s, when an unknown printer took a galley of type and scrambled it to make a type specimen book. It has survived not only five centuries, but also the leap into electronic typesetting, remaining essentially unchanged. It was popularised in the 1960s with the release of Linoform sheets containing Lorem Ipsum passages, and more recently with desktop publishing software like Quillset Layout including versions of Lorem Ipsum.</p>
  <p class="letter body-text para-2">It has survived not only five centuries, but also the leap into electronic typesetting, remaining essentially unchanged. It was popularised in the 1960s with the release of Linoform sheets containing Lorem IpsumIpsum passages.</p>
  <p class="letter closing">Yours Sincerely</p>
  <div class="letter signatory">
    <p class="name">Daniel Carver</p>
    <p class="role">Managing Director</p>
  </div>

  <p class="contact-bar"><b>P:</b> 03 9000 4120 <span class="sep">|</span><b>E:</b> info@harborpeak.example <span class="sep">|</span> www.<span class="domain">harborpeak</span>.example</p>

  <aside class="office-rail">
    <div class="office office-head">
      <h3>Head Office</h3>
      <p>41 Kestrel Way</p>
      <p>Linden Bay</p>
      <p>Victoria 3208</p>
      <p><span class="label">Ph:</span> 03 9000 4120</p>
      <p><span class="label">Fax:</span> 03 9000 4129</p>
    </div>
    <span class="rule" style="top:527px"></span>
    <div class="office office-north">
      <h3>Northgate Office</h3>
      <p>9 Marlow Street</p>
      <p>Northgate Victoria 3634</p>
      <p><span class="label">Ph:</span> 03 5900 2231</p>
      <p><span class="label">Fax:</span> 03 5900 2238</p>
    </div>
    <span class="rule" style="top:667px"></span>
    <div class="office office-west">
      <h3>Westbay Office</h3>
      <p>15 Orwin Court</p>
      <p>Westbay Victoria 3217</p>
      <p><span class="label">Ph:</span> 03 4900 6610</p>
      <p><span class="label">Fax:</span> 03 4900 6618</p>
    </div>
    <span class="rule" style="top:802px"></span>
    <div class="office office-river">
      <h3>Riverton Office</h3>
      <p>Unit 4, 58 Ferncourt Drive</p>
      <p>Riverton Queensland 4117</p>
      <p><span class="label">Ph:</span> 07 3900 8841</p>
      <p><span class="label">Fax:</span> 07 3900 8849</p>
    </div>
  </aside>
</main>
</body>
</html>
```